Cedar Lantern Letterhead

I just need letterhead for my integrative psychiatry business. I'm going to use this to do mailings to other doctors, as well as send letters to patients. Thank you

Business

```html
<!DOCTYPE html>
<html lang="en">
<head>
<meta charset="utf-8">
<title>Cedar Lantern Letterhead</title>
<link href="https://fonts.googleapis.com/css2?family=Lato:wght@400;700&family=Didact+Gothic&family=Dancing+Script:wght@500&display=swap" rel="stylesheet">
<style>
  :root {
    --backdrop-top: #e6ebed;
    --backdrop-bottom: #d6dde0;
    --paper: #ffffff;
    --paper-back: #f1f1f1;
    --leaf-green: #4a7a1a;
    --sprig-green: #6f9a3a;
    --bark-brown: #5a2e0a;
    --band-brown: #4f2707;
    --ink: #3c3c3c;
    --band-text: #ffffff;
  }
  * { margin: 0; padding: 0; box-sizing: border-box; }
  html, body { width: 1200px; height: 927px; overflow: hidden; }
  body {
    position: relative;
    background: linear-gradient(180deg, var(--backdrop-top), var(--backdrop-bottom));
    font-family: "Didact Gothic", "Lato", sans-serif;
  }
  .sheet {
    position: absolute;
    top: 45px;
    width: 512px;
    height: 696px;
    border-radius: 12px;
    overflow: hidden;
  }
  .sheet--front { left: 43px; background: var(--paper); }
  .sheet--back { left: 635px; background: var(--paper-back); }

  .brand {
    position: absolute;
    display: flex;
    align-items: center;
    gap: 6px;
    font-family: "Lato", sans-serif;
    font-weight: 700;
    color: var(--leaf-green);
    white-space: nowrap;
  }
  .brand__dot { border-radius: 50%; background: var(--leaf-green); flex: none; }
  .brand--header { left: 42px; top: 72px; font-size: 17px; }
  .brand--header .brand__dot { width: 12px; height: 12px; }

  .contact {
    position: absolute;
    right: 40px;
    top: 56px;
    text-align: right;
    font-style: normal;
    font-family: "Lato", sans-serif;
    font-weight: 700;
    font-size: 8.6px;
    line-height: 13px;
  }
  .contact__phone { color: var(--leaf-green); }
  .contact__address { color: var(--bark-brown); }
  .header-rule {
    position: absolute;
    left: 45px; top: 101px;
    width: 427px; height: 2px;
    background: var(--bark-brown);
  }

  .sprig { position: absolute; }
  .sprig--left { left: 0; top: 160px; }
  .sprig--right { right: 0; top: 400px; }

  .letter-body {
    position: absolute;
    left: 43px; top: 138px;
    width: 427px;
    font-size: 10.9px;
    line-height: 17.6px;
    color: var(--ink);
    text-align: justify;
  }
  .letter-body p + p { margin-top: 17.6px; }

  .signature { position: absolute; left: 379px; top: 583px; color: var(--ink); }
  .signature__name { font-size: 13px; }
  .signature__title { font-size: 9px; margin-top: 8px; margin-left: 1px; }

  .web-address {
    position: absolute;
    left: 0; right: 0; top: 634px;
    text-align: center;
    font-family: "Lato", sans-serif;
    font-weight: 700;
    font-size: 7.6px;
    letter-spacing: 1.4px;
    color: var(--bark-brown);
  }

  .footer-band {
    position: absolute;
    left: 0; right: 0; bottom: 0;
    height: 44px;
    background: var(--band-brown);
  }
  .brand--footer { left: 26px; top: 15px; font-size: 10px; color: var(--band-text); }
  .brand--footer .brand__dot { width: 7px; height: 7px; background: var(--band-text); }
  .footer-band__tagline {
    position: absolute;
    left: 170px; top: 10px;
    font-family: "Dancing Script", cursive;
    font-size: 16px;
    color: var(--band-text);
    white-space: nowrap;
  }

  .brand--hero { left: 90px; top: 540px; font-size: 44px; gap: 14px; }
  .brand--hero .brand__dot { width: 30px; height: 30px; }
</style>
</head>
<body>

<section class="sheet sheet--front" aria-label="Letterhead page">
  <div class="brand brand--header"><span class="brand__dot"></span>Cedar Lantern</div>

  <address class="contact">
    <div class="contact__phone">555-014-2206</div>
    <div class="contact__phone">555-014-2207</div>
    <div class="contact__address">4720 Harbor Bend Road, Suite 210 Millbrook, CA 95601</div>
  </address>
  <div class="header-rule"></div>

  <svg class="sprig sprig--left" width="36" height="56" role="img" aria-label="Leafy sprig ornament">
    <rect width="36" height="56" rx="10" fill="var(--sprig-green)" opacity="0.55"/>
  </svg>
  <svg class="sprig sprig--right" width="26" height="56" role="img" aria-label="Leafy sprig ornament">
    <rect width="26" height="56" rx="10" fill="var(--sprig-green)" opacity="0.55"/>
  </svg>

  <div class="letter-body">
    <p>Lorem ipsum dolor sit amet, consectetur adipiscing elit. Donec orci purus, luctus vitae dignissim eu, iaculis sed purus. Vivamus faucibus, ipsum nec aliquet viverra, leo mauris condimentum ligula, sit amet sagittis enim ligula quis arcu. Nam egestas tortor id nisi porttitor mattis. In tortor ante, ultricies in suscipit a, tempus non massa. Vivamus et auctor mi. Fusce vel massa nulla. Phasellus nec eros mauris, et scelerisque orci. Donec malesuada orci vitae nulla accumsan porta a id massa.</p>
    <p>Quisque accumsan iaculis magna sit amet fringilla. Maecenas consequat, magna eget tincidunt semper, odio nibh rutrum mi, id feugiat ante nisi eu risus. Vestibulum nunc orci, rhoncus a placerat in, ultricies in mi. Cras mattis varius eros, vel fringilla nisi suscipit eget. Quisque scelerisque sagittis nulla at porttitor. Mauris a justo et tellus interdum tristique. Sed id augue vitae urna euismod commodo aliquet a quam. Pellentesque arcu velit, cursus et malesuada ut, consequat et diam. Nullam erat sem, rhoncus id ullamcorper vitae, rhoncus et arcu. In ultricies ultricies nulla,</p>
    <p>Kut rutrum nisi iaculis at. Donec eu magna a metus ornare faucibus. Fusce aliquet faucibus ultricies. Morbi semper, est id tincidunt gravida, sem arcu adipiscing lacus, ac bibendum nulla leo eu purus. Quisque nec diam sed risus consectetur a ccumsan quis quis nibh. Vestibulum id purus lorem. Donec eu magna a metus ornare faucibus. Fusce aliquet faucibus ultricies. Morbi semper, est id tincidunt gravida, sem arcu adipiscing lacus, ac bibendum nulla leo eu purus. Quisque nec diam sed risus consectetur a ccumsan quis quis nibh. Vestibulum id purus lorem.</p>
  </div>

  <div class="signature">
    <div class="signature__name">Elena Marsh</div>
    <div class="signature__title">Co-Founder &amp; CEO</div>
  </div>

  <div class="web-address">www.cedarlanternhealth.com</div>

  <footer class="footer-band">
    <div class="brand brand--footer"><span class="brand__dot"></span>Cedar Lantern</div>
    <div class="footer-band__tagline">Caring for the whole person, mind and body..</div>
  </footer>
</section>

<section class="sheet sheet--back" aria-label="Letterhead reverse">
  <div class="brand brand--hero"><span class="brand__dot"></span>Cedar Lantern</div>
</section>

</body>
</html>
```